Young Accounting firm needing a captivating business card

We need a business card design that forces the person to look at the card because its either gold foil, plastic, or lettering pop up etc. We already have a logo with a specific gold color and we need to make it pop. We are an accounting firm. I need the words" accounting, payroll, licenses, audits, taxes" somewhere on the business card so as to describe what we do- preferably on the side where the logo is at.

Industry/Entity Type

Accounting

Contact Information for Business Card

Address 48276 9th Ave S Ste 305, Cedar Hollow, OR 98117
Business Phone (360)418-2096
Fax (360)418-2157
Office Cell Phone (360)586-7319

Font styles to use
Serif

Colors
85abd2

Requirements
Must have
• It should state
• "Accounting" "Taxes" "Audits" "Licenses" "Payroll"
Nice to have
• Matte with gold foil, different textures, With Either a textured ivory background or gray blue slate background
Should not have
• colorful colors

```html
<!DOCTYPE html>
<html lang="en">
<head>
<meta charset="utf-8">
<title>PRLedgerco Business Card</title>
<link rel="stylesheet" href="https://fonts.googleapis.com/css2?family=Lato:wght@300;400;700&display=swap">
<style>
  :root {
    --backdrop: #1d1d1f;
    --card: #2b2b2d;
    --gold: #c9a23a;
    --white: #f4f4f2;
    --muted: #b9b9b6;
    --icon-ink: #2b2b2d;
  }
  * { box-sizing: border-box; margin: 0; padding: 0; }
  html, body {
    width: 1200px; height: 943px; overflow: hidden;
    background: var(--backdrop);
    font-family: "Lato", Arial, sans-serif;
  }
  .stage {
    position: relative; width: 1200px; height: 943px;
    display: flex; justify-content: center; align-items: center; gap: 70px;
  }
  .card {
    position: relative; width: 360px; height: 580px;
    background: var(--card); border-radius: 24px;
    box-shadow: 0 18px 40px rgba(0,0,0,.45);
  }
  /* Front */
  .brand {
    display: flex; align-items: center; gap: 10px;
    color: var(--gold); font-weight: 400;
  }
  .brand-mark { width: 14px; height: 14px; background: var(--gold); flex: none; }
  .card-front .brand {
    position: absolute; top: 262px; left: 0; right: 0;
    justify-content: center; font-size: 40px; letter-spacing: .5px;
  }
  .card-front .brand-mark { width: 22px; height: 22px; }
  .services {
    position: absolute; bottom: 40px; left: 0; right: 0;
    text-align: center; color: var(--muted);
    font-size: 13px; font-weight: 300; letter-spacing: .6px;
    white-space: nowrap;
  }
  .services .sep { margin: 0 6px; }
  /* Back */
  .card-back .brand {
    position: absolute; top: 72px; left: 0; right: 0;
    justify-content: center; font-size: 24px;
  }
  .contact {
    position: absolute; top: 250px; left: 0; right: 0;
    text-align: center; color: var(--white);
  }
  .person-name { font-size: 19px; font-weight: 700; }
  .job-title { color: var(--gold); font-size: 13px; letter-spacing: .8px; margin-top: 4px; }
  .icon-row { display: flex; justify-content: center; gap: 6px; margin: 10px 0 8px; }
  .icon-row svg { width: 16px; height: 16px; }
  .contact-line { font-size: 14px; line-height: 22px; }
  .email { margin-top: 6px; }
  .address { margin-top: 34px; font-size: 13px; line-height: 20px; }
</style>
</head>
<body>
<main class="stage">
  <section class="card card-front" aria-label="Card front">
    <div class="brand"><span class="brand-mark"></span><span class="brand-name">PRLedgerco</span></div>
    <p class="services">Accounting<span class="sep">|</span>Taxes<span class="sep">|</span>Audits<span class="sep">|</span>Licenses<span class="sep">|</span>Payroll</p>
  </section>

  <section class="card card-back" aria-label="Card back">
    <div class="brand"><span class="brand-mark"></span><span class="brand-name">PRLedgerco</span></div>
    <div class="contact">
      <h1 class="person-name">Your Name</h1>
      <p class="job-title">JOB TITLE</p>
      <div class="icon-row">
        <svg viewBox="0 0 16 16" aria-label="Phone"><circle cx="8" cy="8" r="8" fill="var(--gold)"/><path d="M5 4.5l1.5-.5 1 2-1 .8a5 5 0 0 0 2.7 2.7l.8-1 2 1-.5 1.5c-3.5.3-6.8-3-6.5-6.5z" fill="var(--icon-ink)"/></svg>
        <svg viewBox="0 0 16 16" aria-label="Fax"><circle cx="8" cy="8" r="8" fill="var(--gold)"/><rect x="4.5" y="6" width="7" height="5" rx="1" fill="var(--icon-ink)"/><rect x="6" y="4" width="4" height="2.5" fill="var(--icon-ink)"/></svg>
        <svg viewBox="0 0 16 16" aria-label="Email"><circle cx="8" cy="8" r="8" fill="var(--gold)"/><rect x="4" y="5" width="8" height="6" rx="1" fill="var(--icon-ink)"/><path d="M4.5 5.5L8 8.5l3.5-3" stroke="var(--gold)" stroke-width=".8" fill="none"/></svg>
        <svg viewBox="0 0 16 16" aria-label="Mobile"><circle cx="8" cy="8" r="8" fill="var(--gold)"/><rect x="5.5" y="3.5" width="5" height="9" rx="1" fill="var(--icon-ink)"/></svg>
      </div>
      <p class="contact-line">(541)418-2096</p>
      <p class="contact-line">(541)418-2157</p>
      <p class="contact-line">(541)586-7319</p>
      <p class="contact-line email">youremail@ledgerco.com</p>
      <p class="address">48276 9th Ave S Ste 305<br>Cedar Hollow, OR 98117</p>
    </div>
  </section>
</main>
</body>
</html>
```